New boutique IT consultancy needs business card

I need a business card and logo for my IT consultancy business, called 'Quenbrylle' . I want it to make me look bigger than I am. I want it to look classy, and modern. Simple design, that will be easy for me to translate into my webpage etc. The business card should be bold, and different.

The logo should emphasise the 'y' as used in quenbrylle

Target Market(s)

IT divisions in other companies

Industry/Entity Type

Business

Contact Information for Business Card

Marcel Thornby
Director
+61 437 819 063
mthornby@quenbrylle-mail.com

```html
<!DOCTYPE html>
<html lang="en">
<head>
<meta charset="utf-8">
<title>Quenbrylle — Business Card</title>
<link rel="stylesheet" href="https://fonts.googleapis.com/css2?family=Barlow:wght@400;500&display=swap">
<style>
  :root {
    --canvas-bg: #e3e3e3;
    --card-black: #2a2a2a;
    --foil-gold: #c99b6c;
    --foil-light: #e6d2bd;
  }
  * { margin: 0; padding: 0; box-sizing: border-box; }
  html, body {
    width: 1200px;
    height: 933px;
    overflow: hidden;
    background: var(--canvas-bg);
  }
  .canvas {
    position: relative;
    width: 1200px;
    height: 933px;
    font-family: "Barlow", Arial, sans-serif;
  }
  .brand-name {
    position: absolute;
    left: 33px;
    top: 56px;
    font-size: 40px;
    font-weight: 400;
    line-height: 1;
    color: var(--foil-gold);
  }
  .business-card {
    position: absolute;
    left: 285px;
    top: 262px;
    width: 607px;
    height: 350px;
    background: var(--card-black);
    color: var(--foil-gold);
  }
  .card-brand-name {
    position: absolute;
    right: 30px;
    top: 56px;
    font-size: 32px;
    font-weight: 400;
    line-height: 1;
    color: var(--foil-gold);
  }
  .card-identity {
    position: absolute;
    right: 341px;
    top: 180px;
    text-align: right;
  }
  .person-name {
    font-size: 26px;
    font-weight: 400;
    letter-spacing: 0.5px;
    line-height: 1;
    text-transform: uppercase;
  }
  .person-role {
    margin-top: 3px;
    font-size: 12px;
    font-weight: 500;
    letter-spacing: 1px;
    color: var(--foil-light);
    text-transform: uppercase;
  }
  .card-divider {
    position: absolute;
    left: 293px;
    top: 154px;
    width: 2px;
    height: 101px;
    background: var(--foil-gold);
  }
  .card-contact {
    position: absolute;
    left: 319px;
    top: 177px;
    list-style: none;
    font-size: 18px;
    line-height: 28px;
  }
</style>
</head>
<body>
  <main class="canvas">
    <div class="brand-name">Quenbrylle</div>

    <section class="business-card" aria-label="Business card front">
      <div class="card-brand-name">Quenbrylle</div>

      <div class="card-identity">
        <p class="person-name">Marcel Thornby</p>
        <p class="person-role">Director</p>
      </div>

      <div class="card-divider"></div>

      <ul class="card-contact">
        <li>+61 437 819 063</li>
        <li>mthornby@quenbrylle-mail.com</li>
      </ul>
    </section>
  </main>
</body>
</html>
```